"Recently Leased" flyer for real estate agency

Looking to have a Recently Leased flyer designed. This will be delivered to apartments and houses closely situated to a property we have recently leased. The idea is to get the attention of owner/landlords in the area that may be considering leasing their property in the future and inform them of the great work we are doing locally. I would like the design to be a two sided flyer using the photoshop (PSD) template below (we would like to be able to edit this once complete should we need to update copy etc in the future). I would like the front page to look like our "for lease sign with the leased sticker on it and copy, I dont want it to look like a typical junk mail flyer.

Target Market(s)

Property owners and investors, male and female aged 28-70

Industry/Entity Type

Real Estate

Font styles to use
Sans Serif

Colors

Designer to choose colors to be used in the design.

Requirements
Must have
• Harbor Keystone Logo
• Contact information
• Copy supplied
Nice to have
• Slick, clean design,
Should not have
• too many colours or too busy a design.
• NO PROPERTY PHOTOS ON FRONT - I want this to be generic and not relate to a specific property image which might confuse people.

```html
<!DOCTYPE html>
<html lang="en">
<head>
<meta charset="utf-8">
<title>Harbor Keystone – Recently Leased Flyer</title>
<link href="https://fonts.googleapis.com/css2?family=Hind:wght@400;500;600&family=Rubik:wght@400;500;700&display=swap" rel="stylesheet">
<style>
  :root{
    --teal:#2aa5b8;
    --teal-deep:#1a7788;
    --band:#1d7f8f;
    --dark:#1d1f21;
    --dark-2:#2a2d30;
    --red:#e0393e;
    --white:#ffffff;
    --muted:#e6e6e6;
    --page:#ffffff;
  }
  *{box-sizing:border-box;margin:0;padding:0}
  html,body{width:1200px;height:1200px;overflow:hidden;background:var(--page)}
  body{position:relative;font-family:"Hind",sans-serif;color:var(--white)}
  .flyer{position:absolute;top:98px;width:462px;height:1005px;background:linear-gradient(180deg,var(--dark-2),var(--dark) 60%);overflow:hidden}
  .flyer--front{left:100px}
  .flyer--back{left:638px;background:linear-gradient(180deg,#151617 0%,var(--dark-2) 45%,var(--dark) 100%)}
  .abs{position:absolute}

  /* front hero */
  .hero{left:0;top:0;width:462px;height:422px;background:linear-gradient(180deg,#bfe3f2 0%,#d7eef6 25%,#7e8f86 55%,#4f6b45 80%,#9aa39c 100%)}
  .hero-wedge{left:0;top:300px}
  .brand{left:0;top:68px;width:462px;text-align:center;font-family:"Rubik",sans-serif;font-weight:500;font-size:27px;letter-spacing:-.3px;color:#111}
  .brand small{display:block;font-size:8px;font-weight:400;letter-spacing:1px;margin-top:1px;padding-left:150px}

  .headline{left:27px;top:412px;width:420px;line-height:1.15}
  .headline .h1{font-family:"Rubik",sans-serif;font-weight:700;font-size:29px;color:var(--teal)}
  .headline .h1 span{color:var(--red)}
  .headline .h2{font-size:24px;font-weight:400}
  .headline .h3{font-size:24px;font-weight:400;color:var(--teal)}
  .headline .h4{font-family:"Rubik",sans-serif;font-size:22px;font-weight:500}

  .lead{left:28px;top:550px;width:410px;font-size:14px;line-height:1.28}
  .ticks{list-style:none;font-size:13px;line-height:1.3}
  .ticks li{position:relative;padding-left:18px;margin-bottom:7px}
  .ticks li::before{content:"";position:absolute;left:0;top:3px;width:9px;height:9px;border:1.2px solid var(--teal);border-radius:50%}
  .ticks li::after{content:"";position:absolute;left:3.5px;top:4.6px;width:2.4px;height:4.4px;border:solid var(--teal);border-width:0 1.3px 1.3px 0;transform:rotate(40deg)}
  .front-ticks{left:28px;top:610px;width:412px}
  .back-ticks{left:28px;top:535px;width:408px;text-align:justify;font-size:13.2px}
  .back-ticks li{margin-bottom:8px}

  /* contact block */
  .band{left:0;top:870px;width:462px;height:120px;background:var(--band)}
  .portrait{left:28px;top:797px;width:90px;height:106px;background:#fff;padding:4px}
  .portrait div{width:100%;height:100%;background:linear-gradient(180deg,#8fb3c6,#a98a74 60%,#6c8fa8)}
  .contact-title{left:138px;top:796px;font-family:"Rubik",sans-serif;font-weight:500;font-size:14.5px;color:var(--teal)}
  .contact-copy{left:138px;top:814px;width:298px;font-size:12.2px;line-height:1.33;text-align:justify}
  .back-copy{left:138px;top:798px;width:298px;font-size:12.2px;line-height:1.33;text-align:justify}
  .name{left:138px;top:876px;font-family:"Rubik",sans-serif;font-weight:700;font-size:19px}
  .role{left:138px;top:898px;font-size:15px}
  .foot{top:936px;font-size:12px;line-height:1.35}
  .foot-left{left:27px}
  .foot-right{left:223px}
  .foot b{font-weight:600;font-size:12.5px}
  .foot-row{display:flex;align-items:center;gap:5px}
  .foot-row svg{flex:none}
  .indent{padding-left:19px}
  .divider{left:206px;top:938px;width:1px;height:46px;background:rgba(255,255,255,.55)}

  /* back photos */
  .photo{background:linear-gradient(135deg,#c9a07a,#8a6a55 45%,#4e5358)}
  .photo-main{left:28px;top:28px;width:406px;height:264px}
  .thumb{top:306px;width:128px;height:118px}
  .thumb-1{left:28px;background:linear-gradient(135deg,#d8c8a8,#b3a285)}
  .thumb-2{left:167px;background:linear-gradient(135deg,#8a8a84,#5d5e5b)}
  .thumb-3{left:306px;background:linear-gradient(135deg,#f1f1ef,#c9c9c5)}
  .sticker{position:absolute;left:-1px;top:-1px}
  .intro{left:28px;top:458px;width:408px;font-family:"Rubik",sans-serif;font-weight:500;font-size:14px;line-height:1.3;color:var(--teal);text-align:justify}
</style>
</head>
<body>

<!-- FRONT -->
<section class="flyer flyer--front">
  <div class="abs hero" role="img" aria-label="Street of modern terraced townhouses with landscaped garden steps under a blue sky"></div>
  <svg class="abs hero-wedge" width="462" height="125" viewBox="0 0 462 125">
    <polygon points="0,125 0,85 150,44 462,122 462,125" fill="var(--dark-2)"/>
    <polygon points="0,100 0,78 112,38 150,44 462,125 430,125 150,58" fill="var(--teal-deep)"/>
    <polygon points="0,92 112,38 150,44 0,100" fill="var(--teal)"/>
    <circle cx="100" cy="34" r="31" fill="#fff" stroke="var(--teal-deep)" stroke-width="3"/>
  </svg>
  <div class="abs brand">HARBOR KEYSTONE<small>AGENCY</small></div>

  <div class="abs headline">
    <div class="h1">We recently <span>leased</span></div>
    <div class="h2">a property in your building or street.</div>
    <div class="h3">Attracting a great reliable tenant and</div>
    <div class="h4">fantastic return for the owner.</div>
  </div>

  <p class="abs lead">We received a high number of enquires and applications for this property and have a database of screened and qualified tenants looking to lease in your area.</p>

  <ul class="abs ticks front-ticks">
    <li>On average we lease properties 2 weeks faster than the Northern Beaches average</li>
    <li>Strong database of tenants actively looking in the area</li>
    <li>All we do is lease property, no sales – so tenanting and managing your property is our priority</li>
    <li>90 day money back guarantee on our level of service</li>
    <li>Highly competitive, simple all-inclusive pricing.</li>
    <li>Experience the difference of a property management specialist</li>
  </ul>

  <div class="abs band"></div>
  <div class="abs portrait"><div role="img" aria-label="Portrait photo of the property manager"></div></div>
  <div class="abs contact-title">CONTACT SAM</div>
  <p class="abs contact-copy">to get your free rental appraisal or transfer your existing investment to an agency that will give it the attention it deserves and maxamise your return.</p>
  <div class="abs name">SAM CARTER</div>
  <div class="abs role">Director/Property Manager</div>
  <div class="abs foot foot-left">
    <div class="foot-row"><svg width="14" height="12" viewBox="0 0 14 12"><path d="M7 0L0 6h2v6h4V8h2v4h4V6h2z" fill="#fff"/></svg><b>Harbor Keystone Agency</b></div>
    <div class="indent">Level 1, 12 Marlow Rd,</div>
    <div class="indent">Fairhaven NSW 2095</div>
  </div>
  <div class="abs divider"></div>
  <div class="abs foot foot-right">
    <div class="foot-row"><svg width="10" height="10" viewBox="0 0 10 10"><path d="M2 0l2 2.5-1.2 1.3a6 6 0 0 0 3.4 3.4L7.5 6 10 8 8.5 10C4 10 0 6 0 1.5z" fill="#fff"/></svg><b>0400 217 563</b></div>
    <div class="foot-row"><svg width="11" height="9" viewBox="0 0 11 9"><rect x=".5" y=".5" width="10" height="8" fill="none" stroke="#fff"/><path d="M.5 .5l5 4 5-4" fill="none" stroke="#fff"/></svg>sam@harborkeystone.com.au</div>
    <div class="foot-row"><svg width="10" height="10" viewBox="0 0 10 10"><circle cx="5" cy="5" r="4.4" fill="none" stroke="#fff"/><path d="M.6 5h8.8M5 .6c-2.5 2.5-2.5 6.3 0 8.8M5 .6c2.5 2.5 2.5 6.3 0 8.8" fill="none" stroke="#fff" stroke-width=".8"/></svg>www.harborkeystone.com.au</div>
  </div>
</section>

<!-- BACK -->
<section class="flyer flyer--back">
  <div class="abs photo photo-main" role="img" aria-label="Leased apartment balcony with brick tiles, glass table and sliding doors">
    <svg class="sticker" width="52" height="52" viewBox="0 0 52 52"><polygon points="0,34 34,0 50,0 0,50" fill="var(--red)"/><text x="19" y="22" transform="rotate(-45 19 22)" text-anchor="middle" fill="#fff" font-family="Hind,sans-serif" font-size="7.5">LEASED</text></svg>
  </div>
  <div class="abs thumb thumb-1" role="img" aria-label="Leased apartment bedroom">
    <svg class="sticker" width="40" height="40" viewBox="0 0 40 40"><polygon points="0,26 26,0 38,0 0,38" fill="var(--red)"/><text x="15" y="17" transform="rotate(-45 15 17)" text-anchor="middle" fill="#fff" font-family="Hind,sans-serif" font-size="6">LEASED</text></svg>
  </div>
  <div class="abs thumb thumb-2" role="img" aria-label="Leased apartment living room">
    <svg class="sticker" width="40" height="40" viewBox="0 0 40 40"><polygon points="0,26 26,0 38,0 0,38" fill="var(--red)"/><text x="15" y="17" transform="rotate(-45 15 17)" text-anchor="middle" fill="#fff" font-family="Hind,sans-serif" font-size="6">LEASED</text></svg>
  </div>
  <div class="abs thumb thumb-3" role="img" aria-label="Leased apartment kitchen">
    <svg class="sticker" width="40" height="40" viewBox="0 0 40 40"><polygon points="0,26 26,0 38,0 0,38" fill="var(--red)"/><text x="15" y="17" transform="rotate(-45 15 17)" text-anchor="middle" fill="#fff" font-family="Hind,sans-serif" font-size="6">LEASED</text></svg>
  </div>

  <p class="abs intro">The fundamental idea behind Harbor Keystone Agency was to give landlords a simple and confidence inspiring experience. We achieve this through:</p>

  <ul class="abs ticks back-ticks">
    <li>Unique marketing that goes beyond the standard listing sites and has seen our average days-on-market at 5.9days for 2018.</li>
    <li>A simple, yet competitive fee structure.</li>
    <li>Excellent customer service through an experienced professional property manager.</li>
    <li>Sound advice and communication through out the leasing and management process.</li>
    <li>A simple yet powerful landlord portal which enables owners to view media rich inspection reports, financial reports and maintenance progress at anytime.</li>
    <li>We then back our service promise with a 90day money back guarantee.</li>
  </ul>

  <div class="abs band"></div>
  <div class="abs portrait"><div role="img" aria-label="Portrait photo of the property manager"></div></div>
  <p class="abs back-copy">If you have been considering leasing your property, purchasing a local investment or aren't happy with your current managing agency, please don't hesitate to contact your local rental specialist for more information:</p>
  <div class="abs name">SAM CARTER</div>
  <div class="abs role">Director/Property Manager</div>
  <div class="abs foot foot-left">
    <div class="foot-row"><svg width="14" height="12" viewBox="0 0 14 12"><path d="M7 0L0 6h2v6h4V8h2v4h4V6h2z" fill="#fff"/></svg><b>Harbor Keystone Agency</b></div>
    <div class="indent">Level 1, 12 Marlow Rd,</div>
    <div class="indent">Fairhaven NSW 2095</div>
  </div>
  <div class="abs divider"></div>
  <div class="abs foot foot-right">
    <div class="foot-row"><svg width="10" height="10" viewBox="0 0 10 10"><path d="M2 0l2 2.5-1.2 1.3a6 6 0 0 0 3.4 3.4L7.5 6 10 8 8.5 10C4 10 0 6 0 1.5z" fill="#fff"/></svg><b>0400 217 563</b></div>
    <div class="foot-row"><svg width="11" height="9" viewBox="0 0 11 9"><rect x=".5" y=".5" width="10" height="8" fill="none" stroke="#fff"/><path d="M.5 .5l5 4 5-4" fill="none" stroke="#fff"/></svg>sam@harborkeystone.com.au</div>
    <div class="foot-row"><svg width="10" height="10" viewBox="0 0 10 10"><circle cx="5" cy="5" r="4.4" fill="none" stroke="#fff"/><path d="M.6 5h8.8M5 .6c-2.5 2.5-2.5 6.3 0 8.8M5 .6c2.5 2.5 2.5 6.3 0 8.8" fill="none" stroke="#fff" stroke-width=".8"/></svg>www.harborkeystone.com.au</div>
  </div>
</section>

</body>
</html>
```